letterhead design using our existing logo

We are a small boutique property management business based in Sydney's Northern Beaches.
We are after a sleek, simple modern letterhead (A4) incorporating our logo and its colours.
Also matching envelope (DL)
I have attached the logo with black text and white text for design options.

Target Market(s)

29-69yo Male and Female

Industry/Entity Type

Property Management

Requirements
Must have
• - Keyhaven Estates logo
• - Address, number and website:
• Suite 7, 18-19 Harlow Parade, Brookvale NSW 2100
• Tel: Tom Carrick 0417 293 608 Lorena Adcock 0409 516 742 www.keyhavenestatesgroup.com.au
Nice to have
• sleek design that looks modern and professional
Should not have
• too many colours or too busy

```html
<!DOCTYPE html>
<html lang="en">
<head>
<meta charset="utf-8">
<title>Keyhaven Estates – Letterhead &amp; Envelope</title>
<link href="https://fonts.googleapis.com/css2?family=Questrial&family=Lato:wght@400;700&display=swap" rel="stylesheet">
<style>
  :root {
    --backdrop: #e4e7e8;
    --sheet: #ffffff;
    --envelope: #efefef;
    --teal: #2b9192;
    --ink: #1a1a1a;
    --body: #3a3a3a;
    --watermark: rgba(150, 160, 160, 0.22);
  }
  * { box-sizing: border-box; margin: 0; padding: 0; }
  html, body { width: 1200px; height: 784px; overflow: hidden; }
  body {
    background: var(--backdrop);
    font-family: "Questrial", sans-serif;
    position: relative;
  }
  .letterhead, .envelope {
    position: absolute;
    top: 45px;
    width: 512px;
    height: 696px;
    border-radius: 14px;
    overflow: hidden;
    box-shadow: 0 1px 4px rgba(0, 0, 0, 0.18);
  }
  .letterhead { left: 42px; background: var(--sheet); }
  .envelope { left: 634px; background: var(--envelope); }

  .brand-name {
    font-family: "Questrial", sans-serif;
    color: var(--ink);
    white-space: nowrap;
    letter-spacing: 0.2px;
  }
  .letterhead .brand-name {
    position: absolute;
    left: 53px;
    top: 56px;
    font-size: 19px;
  }
  .contact {
    position: absolute;
    right: 28px;
    top: 55px;
    text-align: right;
    font-family: "Lato", sans-serif;
    font-weight: 700;
    font-size: 7.6px;
    line-height: 13.5px;
    color: var(--teal);
  }
  .contact .phone { font-weight: 400; color: #333; }
  .header-rule {
    position: absolute;
    left: 56px;
    right: 27px;
    top: 103px;
    height: 2px;
    background: var(--teal);
  }
  .watermark {
    position: absolute;
    left: 86px;
    top: 333px;
    font-size: 32px;
    color: var(--watermark);
    white-space: nowrap;
  }
  .letter-body {
    position: absolute;
    left: 54px;
    top: 143px;
    width: 427px;
    font-size: 10.9px;
    line-height: 17.75px;
    color: var(--body);
    text-align: justify;
    hyphens: auto;
  }
  .letter-body p + p { margin-top: 17.75px; }
  .signature {
    position: absolute;
    left: 391px;
    top: 585px;
    color: var(--body);
  }
  .signature .name { font-size: 14px; }
  .signature .role { font-size: 9.5px; margin-top: 6px; }
  .footer-band {
    position: absolute;
    left: 0;
    right: 0;
    bottom: 0;
    height: 36px;
    background: var(--teal);
    color: #fff;
    font-family: "Lato", sans-serif;
    font-weight: 700;
    font-size: 10px;
    letter-spacing: 2px;
    display: flex;
    align-items: center;
    justify-content: center;
  }
  .envelope .brand-name {
    position: absolute;
    right: 98px;
    top: 566px;
    font-size: 33px;
  }
</style>
</head>
<body>
  <section class="letterhead">
    <div class="brand-name">Keyhaven Estates</div>
    <div class="contact">
      <div>Tom Carrick: <span class="phone">0417 293 608</span></div>
      <div>Lorena Adcock: <span class="phone">0409 516 742</span></div>
      <div>Suite 7, 18-19 Harlow Parade, Brookvale NSW 2100</div>
    </div>
    <div class="header-rule"></div>
    <div class="watermark" aria-hidden="true">Keyhaven Estates</div>
    <div class="letter-body" lang="la">
      <p>Lorem ipsum dolor sit amet, consectetur adipiscing elit. Donec orci purus, luctus vitae dignissim eu, iaculis sed purus. Vivamus faucibus, ipsum nec aliquet viverra, leo mauris condimentum ligula, sit amet sagittis enim ligula quis arcu. Nam egestas tortor id nisi porttitor mattis. In tortor ante, ultricies in suscipit a, tempus non massa. Vivamus et auctor mi. Fusce vel massa nulla. Phasellus nec eros mauris, et scelerisque orci. Donec malesuada orci vitae nulla accumsan porta a id massa.</p>
      <p>Quisque accumsan iaculis magna sit amet fringilla. Maecenas consequat, magna eget tincidunt semper, odio nibh rutrum mi, id feugiat ante nisi eu risus. Vestibulum nunc orci, rhoncus a placerat in, ultricies in mi. Cras mattis varius eros, vel fringilla nisi suscipit eget. Quisque scelerisque sagittis nulla at porttitor. Mauris a justo et tellus interdum tristique. Sed id augue vitae urna euismod commodo aliquet a quam. Pellentesque arcu velit, cursus et malesuada ut, consequat et diam. Nullam erat sem, rhoncus id ullamcorper vitae, rhoncus et arcu. In ultricies ultricies nulla.</p>
      <p>Kut rutrum nisi iaculis at. Donec eu magna a metus ornare faucibus. Fusce aliquet faucibus ultricies. Morbi semper, est id tincidunt gravida, sem arcu adipiscing lacus, ac bibendum nulla leo eu purus. Quisque nec diam sed risus consectetur a ccumsan quis quis nibh. Vestibulum id purus lorem. Donec eu magna a metus ornare faucibus. Fusce aliquet faucibus ultricies. Morbi semper, est id tincidunt gravida, sem arcu adipiscing lacus, ac bibendum nulla leo eu purus. Quisque nec diam sed risus consectetur a ccumsan quis quis nibh. Vestibulum id purus lorem.</p>
    </div>
    <div class="signature">
      <div class="name">Rhys Delaney</div>
      <div class="role">Co-Founder &amp; CEO</div>
    </div>
    <div class="footer-band">www.keyhavenestatesgroup.com.au</div>
  </section>

  <section class="envelope">
    <div class="brand-name">Keyhaven Estates</div>
  </section>
</body>
</html>
```